custom carpentry, woodworking and home repair company needs logo design and business card design

Attention: I apologize but I just received notification from my state that I cannot use the company name that I originally submitted (Beyond The Bench). The new name will be Joinolux We need a company logo and business card design for our new company based in the Hampton Roads area of Virginia. The company name is Joinolux. The final design should give a first impression of true craftsmanship and attention to detail. We would like the card to include the company name, my name Mark Tellman (owner), phone number (757) 348-2615, website (joinolux-example.com) and email address (mark@joinolux-example.com). Everything else is up to your discretion. Thanks, have fun, and good luck.

Industry/Entity Type

Business

Contact Information for Business Card

See project description

Logo Text

see project description

Colors

Designer to choose colors to be used in the design.

```html
<!DOCTYPE html>
<html lang="en">
<head>
<meta charset="utf-8">
<title>Joinolux Business Card</title>
<link href="https://fonts.googleapis.com/css2?family=Montserrat:wght@400;700&display=swap" rel="stylesheet">
<style>
  :root {
    --page: #ffffff;
    --ink: #000000;
    --band: #58585a;
    --paper: #ffffff;
    --brand-text: #ffffff;
  }
  html, body {
    margin: 0;
    width: 1200px;
    height: 1000px;
    overflow: hidden;
    background: var(--page);
  }
  .business-card {
    position: absolute;
    left: 302px;
    top: 301px;
    width: 578px;
    height: 348px;
    background: var(--ink);
    font-family: "Montserrat", Arial, sans-serif;
  }
  .card-shapes {
    position: absolute;
    inset: 0;
  }
  .card-frame {
    position: absolute;
    inset: 0;
    border: 2px solid var(--ink);
    pointer-events: none;
  }
  .brand {
    position: absolute;
    left: 40px;
    width: 192px;
    top: 170px;
    display: flex;
    align-items: center;
    justify-content: center;
    gap: 10px;
  }
  .brand-mark {
    width: 18px;
    height: 18px;
    background: var(--brand-text);
  }
  .brand-name {
    margin: 0;
    color: var(--brand-text);
    font-weight: 700;
    font-size: 22px;
    letter-spacing: 1px;
    text-transform: uppercase;
  }
  .contact {
    position: absolute;
    left: 288px;
    top: 138px;
    color: var(--ink);
  }
  .contact-name {
    margin: 0 0 10px;
    font-weight: 700;
    font-size: 21px;
    line-height: 28px;
  }
  .contact-line {
    margin: 0;
    font-weight: 400;
    font-size: 17px;
    line-height: 22px;
  }
</style>
</head>
<body>
  <div class="business-card">
    <svg class="card-shapes" width="578" height="348" viewBox="0 0 578 348">
      <path class="accent-band" fill="var(--band)" d="M271 0 L578 0 L578 348 L271 348 Q197 174 271 0 Z"/>
      <path class="info-panel" fill="var(--paper)" d="M326 0 L578 0 L578 348 L326 348 Q146 174 326 0 Z"/>
    </svg>
    <div class="card-frame"></div>

    <div class="brand">
      <span class="brand-mark"></span>
      <p class="brand-name">Joinolux</p>
    </div>

    <div class="contact">
      <p class="contact-name">Mark Tellman</p>
      <p class="contact-line">P: (757) 348-2615</p>
      <p class="contact-line">E: mark@joinolux-example.com</p>
      <p class="contact-line">www.joinolux-example.com</p>
    </div>
  </div>
</body>
</html>
```